Pregnancy Wellbeing Coach seeks Book Cover Design

I am a former midwife who now works within alternative healthcare to support women and their families during pregnancy.
I have written a book "Quiet and Carrying Light" which is a pregnancy guide that encourages women to look "outside the box" of conventional medicine ...to find alternative solutions to difficulties that they might be experiencing. So it looks as breathing, meditative and journeying techniques, exercise, connection to nature, communication with the baby...those sort of things.
The book also is a guide for those who support the pregnant women ...the best friend, sister, mother, partner - all those who want to be involved and make a positive contribution to the transformation of the woman into motherhood ...because undoubtedly their lives will be changed by the experience.
It is my belief that we all hold an innate wisdom, the wisdom of our ancestors and that during pregnancy women are connected to the lineage of child bearers back through time ...so it is has a sacred element to it, a time of coming together ... a passing through a doorway, where life will be forever changed.
My website is : www.tessmorrowcalm.example

Thank you :)

Target Market(s)

Pregnant women and those who support them during pregnancy

Industry/Entity Type

Health Care

Font styles to use
Serif
Script

Colors

Designer to choose colors to be used in the design.

Requirements
Must have
• A pregnant woman ...
• Natural World
• Title : Quiet & Carrying Light
• Subtitle : Gentle Practices to Guide A Present-Day Mother's Changing Passage Across Nine Months
• Author: Tess Morrow
Nice to have
• I have a feeling that nature or the natural world is important.
• And the sign of support/community
• And maybe the stars
Should not have
• No Babies
• No "highly polished women"
• No huge pregnant bellies

```html
<!DOCTYPE html>
<html lang="en">
<head>
<meta charset="utf-8">
<title>Quiet and Carrying Light — Tess Morrow</title>
<link rel="stylesheet" href="https://fonts.googleapis.com/css2?family=Josefin+Sans:wght@600&family=Libre+Caslon+Text&display=swap">
<style>
  :root {
    --backdrop: #2a2a2a;
    --cover-top: #fdea12;
    --cover-bottom: #fbc113;
    --ink: #0b0b0d;
    --paper: #f4f1ec;
    --author-red: #d51f2a;
    --blossom: #f6c9d6;
    --blossom-deep: #e98aa6;
  }
  * { margin: 0; padding: 0; box-sizing: border-box; }
  html, body {
    width: 1200px; height: 1200px; overflow: hidden;
    background: var(--backdrop);
  }
  .cover {
    position: absolute; left: 228px; top: 50px;
    width: 744px; height: 1100px;
    background: linear-gradient(180deg, var(--cover-top) 0%, var(--cover-bottom) 100%);
    overflow: hidden;
  }
  .subtitle {
    position: absolute; left: 0; right: 0; top: 82px;
    text-align: center;
    font-family: "Josefin Sans", sans-serif; font-weight: 600;
    font-size: 14px; line-height: 23px; letter-spacing: 0.2em;
    text-transform: uppercase; color: var(--ink);
  }
  .blossom {
    position: absolute; border-radius: 50%; z-index: 1;
    background: radial-gradient(ellipse at center, var(--blossom) 0%, rgba(246,201,214,0.85) 45%, rgba(233,138,166,0) 72%);
  }
  .blossom--upper { left: 500px; top: 180px; width: 280px; height: 340px; }
  .blossom--lower { left: -30px; top: 640px; width: 480px; height: 400px; }
  .title { position: absolute; inset: 0; z-index: 2; font-weight: 400; }
  .title-bar {
    position: absolute;
    background: var(--ink); color: var(--paper);
    font-family: "Libre Caslon Text", serif;
    font-size: 86px; line-height: 1;
    padding: 30px 40px 30px 80px;
    white-space: nowrap;
  }
  .title-bar--first  { left: 53px;  top: 296px; transform: rotate(-0.8deg); }
  .title-bar--second { left: 40px;  top: 440px; padding-left: 44px; padding-right: 40px; transform: rotate(-0.4deg); }
  .title-bar--third  { left: 344px; top: 588px; padding-left: 44px; padding-right: 40px; transform: rotate(-0.7deg); }
  .author {
    position: absolute; left: 135px; top: 957px; z-index: 3;
    width: 474px; height: 68px;
    background: var(--author-red); color: #fff;
    font-family: "Josefin Sans", sans-serif; font-weight: 600;
    font-size: 36px; letter-spacing: 0.22em;
    display: flex; align-items: center; justify-content: center;
    padding-top: 6px; text-transform: uppercase;
  }
</style>
</head>
<body>
  <main class="cover">
    <p class="subtitle">Gentle Practices to Guide<br>A Present-Day Mother's Changing Passage<br>Across Nine Months</p>

    <div class="blossom blossom--upper" role="img" aria-label="Flowering cherry branch with pink blossoms reaching in from the upper right"></div>
    <div class="blossom blossom--lower" role="img" aria-label="Flowering cherry branch with clusters of pink blossoms across the lower left"></div>

    <h1 class="title">
      <span class="title-bar title-bar--first">Quiet</span>
      <span class="title-bar title-bar--second">and Carrying</span>
      <span class="title-bar title-bar--third">Light</span>
    </h1>

    <p class="author">Tess Morrow</p>
  </main>
</body>
</html>
```